Harvest Gathering event flyer

I would like a church event flyer designed. The event is called "HARVEST GATHERING 2018". I am looking for a professional, yet catchy design that uses our brand colors and logo creatively while communicating key information of the event effectively.

1. The logo is attached in two color formats. The designer has the choice to use them as he/she want.

2. The location of the event is: Lindqvist Community Center, 482 Tamsworth Street, Portland, ME 04102
3. Time and date of event. The designer can organize and format the date and time as he/she pleases.
December 28th, 29th @ 7:00PM
December 30th @ 10:00AM
4. The topic of the event is "Tongues of fire". The designer is free to use this phrase as he/she pleases to create a good composition.
5. Speaker: Prophet Marcus Obuya
6. Contact information: contact@cedarbrookfellowship.org - Telephone number: 207 555 0148

7. I would also like the following three words on the flyer. These words describe the focus of the event: FIRE, REVIVAL, PROPHETIC

```html
<!DOCTYPE html>
<html lang="en">
<head>
<meta charset="utf-8">
<title>Harvest Gathering 2018 Flyer</title>
<link href="https://fonts.googleapis.com/css2?family=Russo+One&family=Roboto:ital,wght@0,400;0,700;0,900;1,400&family=Roboto+Condensed:wght@700&display=swap" rel="stylesheet">
<style>
  :root {
    --page-bg: #aac2cf;
    --sky-light: #6fb6ea;
    --sky-mid: #2f7fc7;
    --navy: #173d73;
    --navy-deep: #12305e;
    --orange: #f0901e;
    --white: #ffffff;
    --soft-white: #dfe8f3;
  }
  * { margin: 0; padding: 0; box-sizing: border-box; }
  html, body { width: 1200px; height: 798px; overflow: hidden; }
  body {
    background: var(--page-bg);
    font-family: "Roboto", Arial, sans-serif;
    color: var(--white);
    position: relative;
  }
  .flyer {
    position: absolute;
    left: 340px; top: 29px;
    width: 520px; height: 740px;
    background: linear-gradient(180deg, var(--sky-light) 0%, var(--sky-mid) 35%, var(--navy) 62%, var(--navy-deep) 100%);
    overflow: hidden;
    box-shadow: 0 6px 18px rgba(20, 40, 70, 0.25);
  }
  .hero-visual {
    position: absolute;
    left: 120px; top: 110px;
    width: 400px; height: 320px;
    background: radial-gradient(closest-side at 35% 55%, rgba(255,255,255,0.7) 0%, rgba(190,220,245,0.4) 45%, rgba(47,127,199,0) 100%);
  }
  .event-title {
    position: absolute; left: 34px; top: 30px;
    font-family: "Russo One", "Arial Black", sans-serif;
    font-size: 38px; font-weight: 400; color: var(--orange); letter-spacing: 0.5px;
  }
  .event-year {
    position: absolute; left: 230px; top: 76px;
    font-family: "Russo One", "Arial Black", sans-serif;
    font-size: 36px; color: var(--navy);
  }
  .col-left { position: absolute; left: 40px; top: 380px; width: 215px; }
  .col-right { position: absolute; left: 285px; top: 300px; width: 215px; }
  .date-month { font-family: "Roboto Condensed", sans-serif; font-size: 26px; font-weight: 700; line-height: 1; }
  .date-days { font-size: 58px; font-weight: 900; line-height: 1; }
  .date-time { font-size: 34px; font-weight: 900; line-height: 1; }
  .date-big { font-size: 104px; font-weight: 900; line-height: 0.95; }
  .invite { font-size: 10px; font-weight: 700; letter-spacing: 0.5px; margin-top: 10px; }
  .topic { font-family: "Roboto Condensed", sans-serif; font-size: 24px; font-weight: 700; line-height: 1.05; margin-top: 4px; }
  .venue { font-size: 11px; line-height: 1.35; margin-top: 10px; color: var(--soft-white); text-transform: uppercase; }
  .divider {
    position: absolute; left: 262px; top: 400px;
    width: 2px; height: 110px; background: var(--orange);
  }
  .speaker { margin-top: 22px; font-size: 12px; line-height: 1.3; }
  .speaker-label { font-weight: 900; display: block; }
  .speaker-name { font-style: italic; }
  .focus-words {
    position: absolute; left: 40px; top: 642px;
    font-size: 24px; font-weight: 900; letter-spacing: 1px; line-height: 1;
  }
  .focus-words .sep { font-weight: 400; margin: 0 4px; }
  .brand {
    position: absolute; left: 40px; top: 688px;
    display: flex; align-items: center; gap: 10px;
  }
  .brand-mark { width: 16px; height: 16px; border-radius: 50%; background: var(--orange); }
  .brand-name { font-size: 26px; font-weight: 700; color: var(--white); letter-spacing: 1px; line-height: 1; }
  .contact { position: absolute; left: 272px; top: 678px; font-size: 12px; }
  .contact-row { display: flex; align-items: center; gap: 10px; margin-bottom: 8px; }
  .contact-phone { font-size: 22px; line-height: 1; }
  .contact-row svg { width: 16px; height: 16px; fill: var(--orange); flex: none; }
</style>
</head>
<body>
  <main class="flyer">
    <div class="hero-visual" role="img" aria-label="Photo of the speaker smiling in front of a large cross against a bright cloudy sky"></div>

    <h1 class="event-title">HARVEST GATHERING</h1>
    <div class="event-year">2018</div>

    <section class="col-right">
      <div class="date-month">DECEMBER</div>
      <div class="date-big">30</div>
      <div class="date-time">10:00AM</div>
      <p class="speaker"><span class="speaker-label">SPEAKER:</span><span class="speaker-name">PROPHET MARCUS OBUYA</span></p>
    </section>

    <div class="divider"></div>

    <section class="col-left">
      <div class="date-month">DECEMBER</div>
      <div class="date-days">28,29</div>
      <div class="date-time">07:00PM</div>
      <p class="invite">COME TO JOIN US</p>
      <p class="topic">TONGUES<br>OF FIRE</p>
      <p class="venue">Lindqvist Community Center,<br>482 Tamsworth Street, Port<br>land, ME 04102</p>
    </section>

    <p class="focus-words">FIRE<span class="sep">|</span>REVIVAL<span class="sep">|</span>PROPHETIC</p>

    <div class="brand">
      <span class="brand-mark"></span>
      <span class="brand-name">CEDARBROOK</span>
    </div>

    <div class="contact">
      <div class="contact-row">
        <svg viewBox="0 0 24 24" aria-hidden="true"><path d="M6.6 10.8a15.1 15.1 0 0 0 6.6 6.6l2.2-2.2c.3-.3.7-.4 1-.2 1.1.4 2.3.6 3.6.6.6 0 1 .4 1 1V20c0 .6-.4 1-1 1A17 17 0 0 1 3 4c0-.6.4-1 1-1h3.5c.6 0 1 .4 1 1 0 1.3.2 2.5.6 3.6.1.3 0 .7-.2 1z"/></svg>
        <span class="contact-phone">207 555 0148</span>
      </div>
      <div class="contact-row">
        <svg viewBox="0 0 24 24" aria-hidden="true"><path d="M2 5h20v14H2z M2 5l10 8 10-8" stroke="#12305e" stroke-width="1.5"/></svg>
        <span>contact@cedarbrookfellowship.org</span>
      </div>
    </div>
  </main>
</body>
</html>
```